Awards Banquet Invitation

The Cedar Bluff Area Chamber of Commerce is celebrating it's 65th year at our Annual Awards Banquet (business leader awards). Since we were founded in 1950, we will have a 1950's theme. Dress will be 1950's Formal. I don't want cheesy 1950's. I want Classic feel and fonts from that era. This event is for business professionals so looks from ads in the 50's would be good for inspiration. I would like a look that I can use for the program and event ads. Invitation will include an RSVP insert. Date: February 10, 2015. Time: 6 cocktails, 7 dinner & program, Location: Holm Weide Country Club. Dress is 1950's formal

Target Market(s)

Business owners - our members

Industry/Entity Type

Business

Other font styles liked:
• Lasalle, linotype, thirsty

Colors
86cfc6
474747
ffffff
000000

Requirements
Must have
• classic 50's font and old-fashioned feel
Should not have
• sock hop, soda fountain, 50's diner

```html
<!DOCTYPE html>
<html lang="en">
<head>
<meta charset="utf-8">
<title>65th Anniversary Annual Awards Banquet Invitation</title>
<link rel="stylesheet" href="https://fonts.googleapis.com/css2?family=Crimson+Text:wght@400;700&family=Lobster+Two&family=Dancing+Script:wght@700&display=swap">
<style>
  :root {
    --teal: #86cfc6;
    --teal-bright: #56c3d3;
    --slate: #474747;
    --ink: #000000;
    --paper: #ffffff;
    --pattern-dark: #2f5a5e;
    --panel-soft: #eeeeee;
  }
  * { margin: 0; padding: 0; box-sizing: border-box; }
  html, body { width: 847px; height: 1200px; overflow: hidden; background: var(--ink); }
  .invitation { position: relative; width: 847px; height: 1200px; overflow: hidden; }
  .artwork { position: absolute; inset: 0; }
  .line {
    position: absolute; left: 0; width: 100%; text-align: center; white-space: nowrap;
    transform: translateY(-50%);
  }
  .event-date { top: 33px; font-family: "Lobster Two", cursive; font-size: 29px; color: var(--teal-bright); }
  .venue { top: 69px; font-family: "Crimson Text", serif; font-size: 23px; color: var(--paper); letter-spacing: 0.5px; }
  .invite-lead { top: 434px; font-family: "Crimson Text", serif; font-size: 31px; color: var(--ink); }
  .anniversary { top: 492px; font-family: "Lobster Two", cursive; font-size: 62px; color: var(--teal-bright); }
  .connector { top: 543px; font-family: "Crimson Text", serif; font-size: 22px; color: var(--ink); }
  .event-name { top: 580px; font-family: "Dancing Script", cursive; font-weight: 700; font-size: 42px; color: var(--ink); }
  .host-by { top: 634px; font-family: "Crimson Text", serif; font-size: 22px; color: var(--ink); }
  .host { top: 672px; font-family: "Crimson Text", serif; font-size: 22px; color: var(--ink); }
  .schedule { top: 1063px; font-family: "Crimson Text", serif; font-size: 25px; color: var(--paper); }
  .dress-code { top: 1111px; font-family: "Crimson Text", serif; font-weight: 700; font-size: 25px; color: var(--paper); }
  .dress-code .marker {
    display: inline-block; width: 16px; height: 16px; background: var(--teal-bright);
    transform: rotate(45deg); margin: 0 14px 3px; vertical-align: middle;
  }
</style>
</head>
<body>
<main class="invitation">
  <svg class="artwork" width="847" height="1200" viewBox="0 0 847 1200">
    <defs>
      <linearGradient id="patternTone" x1="0" y1="0" x2="1" y2="1">
        <stop offset="0" stop-color="#3f8f98"/>
        <stop offset="0.5" stop-color="#4aa9b4"/>
        <stop offset="1" stop-color="#3f8f98"/>
      </linearGradient>
    </defs>
    <rect class="pattern-field" width="847" height="1200" fill="url(#patternTone)" role="img" aria-label="Geometric teal and slate starburst tile pattern"/>
    <polygon class="top-wedge" points="0,0 847,0 423.5,300" fill="var(--ink)"/>
    <polygon class="bottom-wedge" points="0,1200 847,1200 423.5,868" fill="var(--ink)"/>
    <polygon class="title-diamond-border" points="10,528 423.5,232 837,528 423.5,827" fill="var(--teal-bright)" stroke="var(--teal-bright)" stroke-width="24" stroke-linejoin="round"/>
    <polygon class="title-diamond" points="24,528 423.5,242 823,528 423.5,817" fill="var(--panel-soft)" stroke="var(--panel-soft)" stroke-width="12" stroke-linejoin="round" role="img" aria-label="Soft white and grey circle tile pattern behind the title"/>
    <line class="rule" x1="182" y1="636" x2="400" y2="636" stroke="var(--slate)" stroke-width="1"/>
    <line class="rule" x1="447" y1="636" x2="666" y2="636" stroke="var(--slate)" stroke-width="1"/>
  </svg>

  <p class="line event-date">February 10, 2015</p>
  <p class="line venue">Holm Weide Country Club</p>

  <p class="line invite-lead">You’re Invited to our</p>
  <h1 class="line anniversary" style="font-weight:400">65th Anniversary</h1>
  <p class="line connector">at the</p>
  <h2 class="line event-name">Annual Awards Banquet</h2>
  <p class="line host-by">by</p>
  <p class="line host">Cedar Bluff Area Chamber of Commerce</p>

  <p class="line schedule">6 cocktails, 7 dinner &amp; program</p>
  <p class="line dress-code">Dress code<span class="marker"></span>1950’s formal</p>
</main>
</body>
</html>
```